New design for www.TrimTable.com

On TrimTable you can find & book your hairdresser. TrimTable is the biggest platform in the Netherlands.

- The design should be a responcive design
- Should be able to go global, should fit in perfectly between all the big booking platforms like roomquay, zipvan etc,
- Should have te result of more bookings. :)
- We are ‘only’ asking a beautiful design, not a technical solution.
- We need a homepage (https://trimtable.com/), search resultpage ((https://trimtable.com/kapper/amsterdam/#), salonpage (https://trimtable.com/kapper/vorden/sol-mira-hair/), about us page (https://trimtable.com/aboutus/), for the hairdresser info page (https://trimtable.com/kapper/), login/register page (https://trimtable.com/account/signin/).

- On the page of the hairdresser there is a dynamic part. The part where you create your appointment. Please take a look at this part too after you choose your treatment (behandeling), employee (medewerker), Date (datum) and time (tijd). The part that you see after this, is the part where you fill in your data as a consumer.

I've added more logo's but mostly we use the green color.

A few of our competitors: www.glowpick.com, www.kestoly.com

Target Market(s)

All consumers

Industry/Entity Type

Hair And Beauty

Number of Pages Required

5+ page

Font styles to use
Sans Serif

Colors
abd036
c3c3c3
757575

Requirements
Must have
• Responsive
• We did an A/B test with the homepage. It turns out that option B works better then option A (take a look at the uploaded pictures). So what we need on the homepage: The USP's with the green checkboxes, The search button needs to by dynamic (changes for example from light green to dark green so you can see you can click it) The call to action sentence Zoek & Vind je kapsalon, the searchfield and searchbutton should be seperated.
Nice to have
• The style that we like is the flat design style. The website should be simple, clean and it should feel a bit like a luxury thing. Because an appointment with the hairdresser can be a real treat and luxury moment for yourself.
• The luxury feeling and flat design that is in the www.zipvan.com website is really nice for example. But then it has to be a bit more light and not so black and dark.

```html
<!DOCTYPE html>
<html lang="nl">
<head>
<meta charset="utf-8">
<title>TrimTable – Kappers in Amsterdam</title>
<link href="https://fonts.googleapis.com/css2?family=Open+Sans:wght@400;600;700&display=swap" rel="stylesheet">
<style>
:root{
  --green:#abd036;
  --green-dark:#8fb21f;
  --grey-light:#c3c3c3;
  --grey:#757575;
  --ink:#2a2a2a;
  --nav:#1d1d1d;
  --panel:#ededed;
  --footer:#1b1b1b;
  --footer-text:#9a9a9a;
  --white:#ffffff;
}
*{box-sizing:border-box;margin:0;padding:0}
html,body{width:716px;height:1200px;overflow:hidden;background:var(--white)}
body{font-family:"Open Sans",Arial,sans-serif;color:var(--ink);font-size:9px;position:relative}

/* navigation */
.site-nav{height:50px;background:var(--nav);display:flex;align-items:center;justify-content:center;gap:4px}
.site-nav a{color:var(--white);text-decoration:none;font-size:8px;font-weight:600;letter-spacing:.4px;padding:0 12px;height:50px;display:flex;align-items:center;white-space:nowrap}
.site-nav a.is-active{background:var(--green)}
.brand{display:flex;flex-direction:column;align-items:center;justify-content:center;padding:0 18px;height:50px}
.brand-mark{width:20px;height:20px;background:var(--green);border-radius:3px;margin-bottom:3px}
.brand-name{font-size:9px;font-weight:700;color:var(--white)}

/* search band */
.search-band{height:268px;background:linear-gradient(180deg,#858585,#6f6f6f);padding-top:26px}
.search-row{display:flex;justify-content:center;gap:6px}
.search-input{width:250px;height:26px;background:var(--white);border-left:5px solid var(--green);display:flex;align-items:center;padding-left:8px;font-size:9px}
.search-button{width:58px;height:26px;background:var(--green);color:var(--white);font-weight:700;font-size:10px;display:flex;align-items:center;justify-content:center}
.search-select{width:124px;height:26px;background:var(--white);display:flex;align-items:center;justify-content:space-between;padding:0 8px;color:var(--grey);font-size:8px}
.search-hint{text-align:center;color:var(--white);font-size:8px;margin-top:6px}
.filters{margin:14px 10px 0;background:var(--panel);height:176px;display:flex;gap:6px;padding:6px}
.filter-col{background:var(--white);padding:7px 8px;font-size:7.5px;color:#444}
.filter-col h4{font-size:7.5px;font-weight:600;margin-bottom:5px}
.col-when{width:150px}
.col-special{width:158px}
.col-org{width:168px}
.col-info{flex:1}
.day-list{list-style:none;border:1px solid var(--grey-light);width:70px;margin-bottom:8px}
.day-list li{padding:2px 5px;border-bottom:1px solid #eee}
.day-list li.is-active{background:var(--green);color:var(--white)}
.day-select{width:110px;height:15px;border:1px solid var(--grey-light);display:flex;align-items:center;justify-content:space-between;padding:0 4px}
.check-list{list-style:none}
.check-list li{display:flex;align-items:center;gap:5px;margin-bottom:3.5px;white-space:nowrap}
.box{width:8px;height:8px;border:1px solid #999;background:var(--white);flex:none}
.info-title{color:var(--green-dark);font-weight:700;margin:12px 0 4px}
.more{text-align:right;margin-top:8px}

/* results */
.results{height:282px;padding-top:24px}
.results h1{text-align:center;font-size:20px;font-weight:400;color:var(--ink)}
.results .intro{text-align:center;font-size:8px;color:#555;width:330px;margin:8px auto 16px;line-height:1.45}
.salon-list{list-style:none;width:472px;margin:0 auto}
.salon{display:flex;align-items:center;height:30px;border-bottom:1px solid #e6e6e6;font-size:7.5px;white-space:nowrap}
.salon-name{width:108px;font-weight:600;overflow:hidden}
.salon-address{width:122px;overflow:hidden}
.salon-distance{width:86px;color:var(--grey-light);font-size:7px}
.salon-rating{display:flex;width:64px}
.salon-count{width:30px;color:#555}
.salon-link{background:var(--green);color:var(--white);font-weight:600;padding:4px 0;width:48px;text-align:center;font-size:7.5px;text-decoration:none;margin-left:auto}

/* map */
.map{height:325px;position:relative;background:linear-gradient(135deg,#f4f4f4,#dcdcdc)}
.map-zoom{position:absolute;right:18px;bottom:30px;display:flex;flex-direction:column;gap:6px}
.map-zoom span{width:16px;height:16px;border-radius:50%;background:var(--green);color:var(--white);font-weight:700;font-size:11px;display:flex;align-items:center;justify-content:center}

/* newsletter */
.newsletter{height:50px;background:#2c2c2c;display:flex;align-items:center;justify-content:center;gap:12px}
.newsletter p{color:var(--green);font-size:9px}
.newsletter-input{width:120px;height:16px;background:#555;color:#aaa;font-size:7px;display:flex;align-items:center;justify-content:space-between;padding:0 5px}

/* footer */
.site-footer{height:225px;background:var(--footer);color:var(--footer-text);padding:22px 36px 0;font-size:7.5px}
.footer-top{display:flex;justify-content:space-between}
.footer-about{width:300px;line-height:1.55}
.footer-about strong{display:block;color:var(--white);font-weight:400;margin-bottom:8px}
.footer-links{display:flex;gap:20px;margin-top:28px}
.footer-links ul{list-style:none;line-height:1.5}
.footer-bottom{display:flex;justify-content:space-between;margin-top:28px;border-top:1px solid #333;padding-top:16px}
.footer-bottom h5{color:var(--white);font-size:9px;font-weight:600;margin-bottom:6px}
.footer-block{width:150px;line-height:1.5}
.social{display:flex;gap:5px;margin-top:2px}
.social span{width:14px;height:14px;background:#3a3a3a;border-radius:2px}
</style>
</head>
<body>

<svg width="0" height="0" style="position:absolute">
  <defs><polygon id="star" points="5,0 6.5,3.5 10,3.8 7.3,6 8.1,9.7 5,7.8 1.9,9.7 2.7,6 0,3.8 3.5,3.5"/></defs>
</svg>

<nav class="site-nav">
  <a href="#">HOME</a>
  <a href="#" class="is-active">ZOEKEN</a>
  <a href="#">SALON</a>
  <div class="brand"><span class="brand-mark"></span><span class="brand-name">TrimTable</span></div>
  <a href="#">ABOUT US</a>
  <a href="#">KAPPERSSITE</a>
  <a href="#">LOGIN/REGISTER</a>
</nav>

<section class="search-band">
  <div class="search-row">
    <div class="search-input">Amsterdam, Nederland</div>
    <div class="search-button">ZOEK</div>
    <div class="search-select">Alle afstanden <span>▾</span></div>
  </div>
  <p class="search-hint">of zoek op plaatsnaam</p>

  <div class="filters">
    <div class="filter-col col-when">
      <h4>Toon salons vind een plek voor:</h4>
      <ul class="day-list">
        <li class="is-active">Vandaag</li><li>Morgen</li><li>Overmorgen</li><li>Middag</li><li>Avond</li>
      </ul>
      <h4>Open op:</h4>
      <div class="day-select">Selecteer een dag <span>▾</span></div>
    </div>
    <div class="filter-col col-special">
      <h4>Ik zoek iets specialistisch:</h4>
      <ul class="check-list">
        <li><span class="box"></span>Black hair</li>
        <li><span class="box"></span>Krullen knippen</li>
        <li><span class="box"></span>Afro</li>
        <li><span class="box"></span>Highlights</li>
        <li><span class="box"></span>Haarwerk</li>
        <li><span class="box"></span>Natuurkleuring</li>
        <li><span class="box"></span>Extensions</li>
      </ul>
    </div>
    <div class="filter-col col-org">
      <h4>Organisaties</h4>
      <ul class="check-list">
        <li><span class="box"></span>Kappersgilde Noord</li>
        <li><span class="box"></span>Salonkring Oost</li>
        <li><span class="box"></span>Keurmerk Salons</li>
        <li><span class="box"></span>Stylistennet</li>
        <li><span class="box"></span>Coiffure Circle</li>
        <li><span class="box"></span>Haarvakunie</li>
        <li><span class="box"></span>TC Atelier Coiffure Breda</li>
      </ul>
    </div>
    <div class="filter-col col-info">
      <ul class="check-list"><li><span class="box"></span>Ik wil betalen met kortingsbon</li></ul>
      <p class="info-title">Kapper Amsterdam</p>
      <p>Makkelijk online je afspraak maken bij een kapper in Amsterdam.</p>
      <p class="more">meer</p>
    </div>
  </div>
</section>

<section class="results">
  <h1>11 kappers gevonden in Amsterdam</h1>
  <p class="intro">Kies een kapper in Amsterdam en maak gelijk je afspraak. Wanneer jij wil en kan maak je online direct je afspraak bij een kapper in Amsterdam.</p>
  <ul class="salon-list">
    <li class="salon"><span class="salon-name">Lina's Haarstudio</span><span class="salon-address">Lindengracht 24, Westerpark</span><span class="salon-distance">(28 km van Amsterdam)</span>
      <span class="salon-rating"><svg width="60" height="10" viewBox="0 0 60 10" fill="#c3c3c3"><use href="#star"/><use href="#star" x="12"/><use href="#star" x="24"/><use href="#star" x="36"/><use href="#star" x="48"/></svg></span>
      <span class="salon-count">(107)</span><a class="salon-link" href="#">Naar salon</a></li>
    <li class="salon"><span class="salon-name">Haarhuis Den Veld</span><span class="salon-address">Dorpsweg 118a, Den Veld</span><span class="salon-distance">(39 km van Amsterdam)</span>
      <span class="salon-rating"><svg width="60" height="10" viewBox="0 0 60 10"><g fill="#2a2a2a"><use href="#star"/><use href="#star" x="12"/><use href="#star" x="24"/><use href="#star" x="36"/></g><use href="#star" x="48" fill="#c3c3c3"/></svg></span>
      <span class="salon-count">(9)</span><a class="salon-link" href="#">Naar salon</a></li>
    <li class="salon"><span class="salon-name">Joris Kappers</span><span class="salon-address">Molenstraat 86, Weesperhoek</span><span class="salon-distance">(51 km van Amsterdam)</span>
      <span class="salon-rating"><svg width="60" height="10" viewBox="0 0 60 10" fill="#c3c3c3"><use href="#star"/><use href="#star" x="12"/><use href="#star" x="24"/><use href="#star" x="36"/><use href="#star" x="48"/></svg></span>
      <span class="salon-count">(0)</span><a class="salon-link" href="#">Naar salon</a></li>
    <li class="salon"><span class="salon-name">Mara Coiffure</span><span class="salon-address">Kerkplein 4, Tiel</span><span class="salon-distance">(65 km van Amsterdam)</span>
      <span class="salon-rating"><svg width="60" height="10" viewBox="0 0 60 10" fill="#c3c3c3"><use href="#star"/><use href="#star" x="12"/><use href="#star" x="24"/><use href="#star" x="36"/><use href="#star" x="48"/></svg></span>
      <span class="salon-count">(0)</span><a class="salon-link" href="#">Naar salon</a></li>
    <li class="salon"><span class="salon-name">Kapsalon Noorderlicht</span><span class="salon-address">Havenkade 15, Paddijk</span><span class="salon-distance">(69 km van Amsterdam)</span>
      <span class="salon-rating"><svg width="60" height="10" viewBox="0 0 60 10" fill="#c3c3c3"><use href="#star"/><use href="#star" x="12"/><use href="#star" x="24"/><use href="#star" x="36"/><use href="#star" x="48"/></svg></span>
      <span class="salon-count">(0)</span><a class="salon-link" href="#">Naar salon</a></li>
  </ul>
</section>

<section class="map" role="img" aria-label="Kaart van Amsterdam met de locaties van de gevonden kapsalons">
  <div class="map-zoom"><span>+</span><span>−</span></div>
</section>

<section class="newsletter">
  <p>Laatste TrimTable tips krijgen? Schrijf je in!</p>
  <div class="newsletter-input">Vul je e-mailadres in <span>›</span></div>
</section>

<footer class="site-footer">
  <div class="footer-top">
    <div class="footer-about">
      <strong>Maak een afspraak bij de kapper in een van deze plaatsen</strong>
      Hier vind je kappers en salons in alle grote en kleine plaatsen van Nederland. Kies je woonplaats en bekijk direct welke kappers er vrije plekken hebben. Vergelijk prijzen, lees ervaringen van andere klanten en boek zonder te bellen. Zo heb je altijd snel een afspraak bij een kapper die bij je past, wanneer het jou uitkomt.
    </div>
    <div class="footer-links">
      <ul><li>Kapper Amsterdam</li><li>Kapper Rotterdam</li><li>Kapper Den Haag</li><li>Kapper Utrecht</li></ul>
      <ul><li>Kapper Eindhoven</li><li>Kapper Tilburg</li><li>Kapper Almere</li><li>Kapper Groningen</li></ul>
      <ul><li>Kapper Breda</li><li>Kapper Nijmegen</li><li>Kapper Haarlem</li><li>Kapper Arnhem</li></ul>
    </div>
  </div>
  <div class="footer-bottom">
    <div class="footer-block">
      <h5>TrimTable</h5>
      <p>Over ons</p><p>Laat ons weten</p>
    </div>
    <div class="footer-block">
      <h5>TrimTable</h5>
      <div class="social"><span></span><span></span><span></span></div>
    </div>
    <div class="footer-block">
      <h5>TrimTable</h5>
      <p>Ben jij een kapper en wil je jezelf op TrimTable? Log hier in</p>
    </div>
  </div>
</footer>

</body>
</html>
```